Zenith Grease street sign

looking for a fresh new looking street sign .. sized 6ft tall 5ft wide <br/>"Zenith Grease<br/>The Velocity Crew"<br/>remove "... and Tune"<br/>remove "Kravo" the bottom should just read "The Velocity Crew"

Target Market(s)

motorist passing my location

Industry/Entity Type

Automotive

Font styles to use
Sans Serif

Requirements
Must have
• Zenith Grease
• The Velocity Crew
Should not have
• NO reference to "Kravo"

```html
<!DOCTYPE html>
<html lang="en">
<head>
<meta charset="utf-8">
<title>Zenith Grease &amp; Repair – Street Sign</title>
<link rel="stylesheet" href="https://fonts.googleapis.com/css2?family=Archivo+Black&family=Libre+Bodoni:wght@700&display=swap">
<style>
  :root {
    --sign-red: #ec1c24;
    --sign-red-deep: #c8161e;
    --sign-navy-top: #1b1c42;
    --sign-navy-bottom: #161a5c;
    --sign-white: #ffffff;
    --sign-ink: #000000;
    --sign-edge: #d4d4d4;
    --flag-tone-light: #e6e6e6;
    --flag-tone-dark: #6b6b6b;
  }
  html, body {
    margin: 0;
    padding: 0;
    width: 960px;
    height: 1200px;
    overflow: hidden;
    background: var(--sign-white);
  }
  .sign-canvas {
    display: block;
    width: 960px;
    height: 1200px;
  }
  .brand-line {
    font-family: "Archivo Black", "Arial Black", sans-serif;
    fill: var(--sign-red);
    stroke: var(--sign-ink);
    stroke-width: 5px;
    stroke-linejoin: round;
    paint-order: stroke fill;
    text-anchor: middle;
  }
  .tagline {
    font-family: "Libre Bodoni", "Times New Roman", serif;
    font-weight: 700;
    fill: var(--sign-white);
    text-anchor: middle;
  }
</style>
</head>
<body>
<svg class="sign-canvas" viewBox="0 0 960 1200" xmlns="http://www.w3.org/2000/svg">
  <defs>
    <linearGradient id="navy-field" x1="0" y1="0" x2="0" y2="1">
      <stop offset="0" stop-color="var(--sign-navy-top)"/>
      <stop offset="1" stop-color="var(--sign-navy-bottom)"/>
    </linearGradient>
    <linearGradient id="red-swoosh" x1="0" y1="0" x2="1" y2="0">
      <stop offset="0" stop-color="var(--sign-red-deep)"/>
      <stop offset="0.5" stop-color="var(--sign-red)"/>
      <stop offset="1" stop-color="var(--sign-red-deep)"/>
    </linearGradient>
    <linearGradient id="flag-fill" x1="0" y1="0" x2="1" y2="1">
      <stop offset="0" stop-color="var(--flag-tone-light)"/>
      <stop offset="1" stop-color="var(--flag-tone-dark)"/>
    </linearGradient>
  </defs>

  <!-- sign panel -->
  <rect class="sign-panel" x="43.5" y="76.5" width="873" height="1047" fill="var(--sign-white)" stroke="var(--sign-edge)" stroke-width="1"/>

  <!-- red swoosh band -->
  <path class="swoosh-band" d="M43 652 Q480 884 917 652 L917 692 Q480 868 43 692 Z" fill="url(#red-swoosh)"/>

  <!-- navy lower field -->
  <path class="navy-field" d="M43 692 Q480 868 917 692 L917 1124 L43 1124 Z" fill="url(#navy-field)"/>

  <!-- brand name -->
  <text class="brand-line brand-line--top" x="478" y="316" font-size="228" textLength="784" lengthAdjust="spacingAndGlyphs">ZENITH</text>
  <text class="brand-line brand-line--middle" x="480" y="512" font-size="228" textLength="660" lengthAdjust="spacingAndGlyphs">GREASE</text>
  <text class="brand-line brand-line--service" x="483" y="658" font-size="142" textLength="610" lengthAdjust="spacingAndGlyphs">&amp; Repair</text>

  <!-- crossed checkered racing flags -->
  <rect class="racing-flags" x="362" y="700" width="234" height="144" rx="10" fill="url(#flag-fill)" role="img" aria-label="Two crossed black and white checkered racing flags"/>

  <!-- crew tagline -->
  <text class="tagline tagline--lead" x="480" y="952" font-size="112" textLength="136" lengthAdjust="spacingAndGlyphs">The</text>
  <text class="tagline tagline--crew" x="480" y="1052" font-size="112" textLength="696" lengthAdjust="spacingAndGlyphs">Velocity Crew</text>
</svg>
</body>
</html>
```